Need Letterhead Design & Matching Business Card

I have a logo that I love already. But the letterhead is less than appealing and boring. I'd like a design for my letterhead which I will match with business cards. Also, I'd like to have used fonts that are generally available, as my current letterhead uses a font named "SPACE" which nobody has unless they download it...so when a Word version is forwarded, it looks awful on the receiver's screed due to not having the font. That being said, modern is the look we like and are going for.

My business is "Hollister Brantley PC" - a law firm specializing in representing people who have suffered catastrophic injuries or death (plane, auto, train crashes etc.).

See attached letterhead, which has all of the pertinent information. My logo is also attached in various formats.

```html
<!DOCTYPE html>
<html lang="en">
<head>
<meta charset="utf-8">
<title>Hollister Brantley PC — Business Card</title>
<link rel="stylesheet" href="https://fonts.googleapis.com/css2?family=Jost:wght@300;400&family=Arimo:wght@400;700&display=swap">
<style>
  :root {
    --page: #ececea;
    --card-light: #f7f7f6;
    --card-dark: #2a2a2a;
    --ink: #1f1f1f;
    --ink-soft: #6d6d6d;
    --rule: #4a4a4a;
    --name-on-dark: #d4d4d4;
  }
  * { box-sizing: border-box; margin: 0; padding: 0; }
  html, body {
    width: 1200px; height: 802px; overflow: hidden;
    background: var(--page);
  }
  .stage { position: relative; width: 1200px; height: 802px; }
  .card {
    position: absolute; top: 246px;
    width: 540px; height: 309px;
    box-shadow: 0 2px 6px rgba(0,0,0,0.12);
  }
  .card--front { left: 40px; background: var(--card-light); color: var(--ink); }
  .card--back  { left: 620px; background: var(--card-dark); }

  .brand-mark {
    position: absolute; top: 48px; right: 128px;
    width: 46px; height: 46px;
    background: var(--ink);
  }

  .firm-name {
    font-family: "Jost", sans-serif; font-weight: 300;
    text-transform: uppercase; letter-spacing: 1px;
    white-space: nowrap;
  }
  .card--front .firm-name {
    position: absolute; right: 36px; top: 108px;
    font-size: 18px; line-height: 24px; color: var(--ink);
  }
  .card--back .firm-name {
    position: absolute; right: 40px; bottom: 42px;
    font-size: 24px; letter-spacing: 1.5px; color: var(--name-on-dark);
  }

  .divider {
    position: absolute; left: 36px; right: 36px; top: 138px;
    border-top: 1px solid var(--rule);
  }
  .person {
    position: absolute; left: 36px; top: 100px;
    font-family: "Arimo", sans-serif;
  }
  .person__name { font-weight: 700; font-size: 13.5px; line-height: 17px; color: var(--ink); }
  .person__title { font-size: 12.5px; line-height: 16px; color: var(--ink-soft); margin-top: 2px; }

  .address {
    position: absolute; right: 36px; top: 156px;
    text-align: right; font-style: normal;
    font-family: "Arimo", sans-serif; font-size: 12.5px; line-height: 18px;
    color: var(--ink-soft);
  }

  .contacts {
    position: absolute; left: 36px; bottom: 34px;
    list-style: none;
    font-family: "Arimo", sans-serif; font-size: 12.5px; color: var(--ink-soft);
  }
  .contacts li { display: flex; align-items: center; gap: 7px; line-height: 19px; }
  .contacts svg { width: 11px; height: 11px; flex: none; }
</style>
</head>
<body>
<main class="stage">
  <section class="card card--front" aria-label="Business card front">
    <div class="brand-mark" aria-hidden="true"></div>
    <p class="firm-name">Hollister Brantley PC</p>

    <div class="person">
      <p class="person__name">Morgan T. Reyes Calder, Esq.</p>
      <p class="person__title">President</p>
    </div>
    <div class="divider"></div>

    <address class="address">
      4820 Larkmont Ave.<br>
      suite 1200, Westbury Hills, CA 90000
    </address>

    <ul class="contacts">
      <li>
        <svg viewBox="0 0 12 12" aria-hidden="true"><circle cx="6" cy="6" r="5.5" fill="#555"/><path d="M4 3.2l1 1.4-.6.8c.4.8 1 1.4 1.8 1.8l.8-.6 1.4 1-.6 1.2C5.6 8.8 3.2 6.4 3 4l1-.8z" fill="#fff"/></svg>
        (555) 014-2276
      </li>
      <li>
        <svg viewBox="0 0 12 12" aria-hidden="true"><rect x="1" y="2.5" width="10" height="7" fill="none" stroke="#555" stroke-width="1.2"/><path d="M1 2.5l5 4 5-4" fill="none" stroke="#555" stroke-width="1.2"/></svg>
        mcalder@hollisterbrantley.com
      </li>
      <li>
        <svg viewBox="0 0 12 12" aria-hidden="true"><circle cx="6" cy="6" r="5.5" fill="#555"/><path d="M.5 6h11M6 .5v11M2 3.5h8M2 8.5h8" stroke="#fff" stroke-width=".8"/></svg>
        www.hollisterbrantley.com
      </li>
    </ul>
  </section>

  <section class="card card--back" aria-label="Business card back">
    <p class="firm-name">Hollister Brantley PC</p>
  </section>
</main>
</body>
</html>
```